Redesign of business card for Birchline Mechanical

We are looking for a new design for our business cards for Birchline Mechanical. We are a plumbing & HVAC construction company, operating on the West Coast of Canada and USA. Logo attached.
Industry/Entity Type
Construction - Plumbing & HVAC
Contact Information for Business Card
Name, address, phone numbers, email, website address
Look and feel
Each slider illustrates characteristics of the customer's brand and the style your logo design should communicate.

```html
<!DOCTYPE html>
<html lang="en">
<head>
<meta charset="utf-8">
<title>Birchline Mechanical — Business Card</title>
<link href="https://fonts.googleapis.com/css2?family=Montserrat:wght@400;500;700;800&display=swap" rel="stylesheet">
<style>
  :root {
    --backdrop: #d3d3d3;
    --paper: #f1f1ef;
    --ink: #141414;
    --ink-soft: #6a6a6a;
    --rule: #2a2a2a;
    --card-black: #0d0d0d;
    --white: #ffffff;
  }
  * { box-sizing: border-box; margin: 0; padding: 0; }
  html, body {
    width: 1200px; height: 1051px; overflow: hidden;
    background: var(--backdrop);
    font-family: "Montserrat", sans-serif;
  }
  .sheet {
    width: 1200px; height: 1051px;
    display: flex; align-items: center; justify-content: center; gap: 60px;
  }
  .card {
    width: 520px; height: 297px;
    border-radius: 4px;
    box-shadow: 0 14px 30px rgba(0,0,0,0.18);
    position: relative;
  }
  .card--front { background: var(--paper); color: var(--ink); }
  .card--back {
    background: var(--card-black); color: var(--white);
    display: flex; align-items: center; justify-content: center;
  }
  .brand {
    display: flex; align-items: center; gap: 10px;
    font-weight: 700; text-transform: uppercase; letter-spacing: 0.04em;
  }
  .brand__square { width: 18px; height: 18px; background: currentColor; flex: none; }
  .card--front .brand {
    position: absolute; left: 26px; top: 60px; width: 200px;
    font-size: 19px; line-height: 1.2;
  }
  .card--back .brand { font-size: 28px; gap: 14px; }
  .card--back .brand__square { width: 26px; height: 26px; }

  .details {
    position: absolute; left: 262px; top: 34px; width: 234px;
  }
  .person__name { font-weight: 800; font-size: 17px; letter-spacing: 0.02em; text-transform: uppercase; }
  .person__title { font-size: 12px; color: var(--ink-soft); margin-top: 2px; }
  .rule { border: 0; border-top: 1px solid var(--rule); margin: 12px 0; }
  .address { font-size: 11.5px; color: var(--ink-soft); line-height: 1.45; }
  .contact { list-style: none; font-size: 11.5px; color: var(--ink-soft); line-height: 1.6; }
  .contact li { display: flex; align-items: center; gap: 7px; }
  .contact svg { width: 11px; height: 11px; fill: var(--ink); flex: none; }
  .contact .tag { color: var(--ink); font-weight: 500; }
</style>
</head>
<body>
<main class="sheet">
  <section class="card card--front">
    <div class="brand"><span class="brand__square"></span><span>Birchline Mechanical</span></div>
    <div class="details">
      <h1 class="person__name">Marcus Thorne</h1>
      <p class="person__title">President</p>
      <hr class="rule">
      <p class="address">4127 Alder Crest Road<br>Suite 210, Tustin, CA 92780<br>2250 Harbor Point Blvd,<br>Suite #415 Tacoma, WA 98402</p>
      <hr class="rule">
      <ul class="contact">
        <li><svg viewBox="0 0 24 24"><path d="M6.6 10.8a15 15 0 006.6 6.6l2.2-2.2c.3-.3.7-.4 1-.2 1.1.4 2.3.6 3.6.6.6 0 1 .4 1 1V20c0 .6-.4 1-1 1A17 17 0 013 4c0-.6.4-1 1-1h3.5c.6 0 1 .4 1 1 0 1.3.2 2.5.6 3.6.1.3 0 .7-.2 1z"/></svg>1-866-555-0147 <span class="tag">Toll Free</span></li>
        <li><svg viewBox="0 0 24 24"><path d="M6.6 10.8a15 15 0 006.6 6.6l2.2-2.2c.3-.3.7-.4 1-.2 1.1.4 2.3.6 3.6.6.6 0 1 .4 1 1V20c0 .6-.4 1-1 1A17 17 0 013 4c0-.6.4-1 1-1h3.5c.6 0 1 .4 1 1 0 1.3.2 2.5.6 3.6.1.3 0 .7-.2 1z"/></svg>213-555-0192</li>
        <li><svg viewBox="0 0 24 24"><path d="M2 5h20v14H2z M2 5l10 8 10-8" /></svg>info@birchlinemech.com</li>
        <li><svg viewBox="0 0 24 24"><circle cx="12" cy="12" r="10"/></svg>www.birchlinemech.com</li>
      </ul>
    </div>
  </section>
  <section class="card card--back">
    <div class="brand"><span class="brand__square"></span><span>Birchline Mechanical</span></div>
  </section>
</main>
</body>
</html>
```